Landing Page für Kornwiese-Prüfset.de
Zielgruppe
Domain: Kornwiese-Prüfset.de
THC Schnelltests mit gringer Anzeigegrenze mit 5ng/ml, ausgerichtet auf die Selbstkontrolle für die Fahrtauglichkeit (Grenze im Gesetz 3,5ng/ml)
Farbe: grün
Anregung siehe Bild
Aufgabenstellung
- Conversionoptimiert
- Soll auf unseren Webshop www.rv-vitalis.de verlinken

```html
<!DOCTYPE html>
<html lang="de">
<head>
<meta charset="utf-8">
<title>Kornwiese-Prüfset.de – Mach den Selbsttest</title>
<link rel="stylesheet" href="https://fonts.googleapis.com/css2?family=Barlow:ital,wght@0,400;0,700;0,800;1,400;1,700;1,800;1,900&family=Source+Sans+3:wght@400;600&display=swap">
<style>
:root{
  --green-dark:#234f1e;
  --green:#2c5e24;
  --green-light:#5f8a5a;
  --cream:#fdf4d9;
  --cream-text:#fbf1cf;
  --orange:#f0a11a;
  --footer:#4b4b4b;
  --body-text:#2c5e24;
}
*{box-sizing:border-box;margin:0;padding:0}
html,body{width:1200px;height:2569px;overflow:hidden;background:#fff}
body{position:relative;font-family:"Source Sans 3",Arial,sans-serif;color:var(--body-text)}
.abs{position:absolute}
.heading{font-family:"Barlow",Arial,sans-serif;font-style:italic;font-weight:800;text-transform:uppercase}
.brand{font-family:"Barlow",Arial,sans-serif;font-weight:800;letter-spacing:.5px}

.hero{left:0;top:0;width:1200px;height:537px;overflow:hidden}
.hero-photo{position:absolute;inset:0;background:radial-gradient(circle at 920px 300px,#3f8c3a 0,#2b6a2a 25%,#1f4d1c 60%,#183f16 100%)}
.hero-band{position:absolute;left:0;top:0}
.hero .brand{left:88px;top:56px;font-size:40px;color:var(--cream-text)}
.hero-title{left:145px;top:182px;font-size:76px;line-height:74px;color:var(--cream-text)}
.hero-sub{left:145px;top:340px;font-family:"Barlow",sans-serif;font-style:italic;font-size:29px;color:var(--cream-text);text-transform:uppercase}
.bubble{left:686px;top:145px}
.bubble-text{left:722px;top:176px;width:130px;font-size:15.5px;line-height:16px;color:var(--green-dark)}

.partner{top:568px;height:50px;background:#e9eee8;border-radius:8px}

.tile{overflow:hidden}
.tile-fill{position:absolute;inset:0}
.tile-title{font-size:37px;line-height:43px;color:var(--cream-text)}
.tile-sub{font-family:"Barlow",sans-serif;font-style:italic;font-size:22px;color:var(--cream-text);text-transform:uppercase}

.section-title{font-size:23px;line-height:26px;color:var(--green-dark)}
.rule{width:68px;height:8px;background:var(--green-dark)}
.copy{font-size:13.2px;line-height:19px;color:var(--body-text)}
.copy p{margin-bottom:18px}

.cta{left:88px;top:1689px;width:1027px;height:65px;border-radius:33px;background:var(--orange);color:#fff;font-size:19px;display:flex;align-items:center;justify-content:center;text-decoration:none}

.field{background:var(--cream);font-size:13px;color:#555;padding:13px 19px}
.check{left:88px;top:2323px;width:18px;height:18px;background:var(--cream)}
.consent{left:113px;top:2323px;font-size:15px;color:#444}
.consent a{color:var(--orange);text-decoration:none}
.send{left:88px;top:2383px;width:259px;height:66px;border-radius:33px;background:var(--green-dark);color:#fff;font-size:18px;display:flex;align-items:center;justify-content:center}
.divider{left:726px;top:1950px;width:1px;height:392px;background:#e2e2e2}
.contact-brand{left:769px;top:1962px;font-size:40px;color:var(--green-dark)}
.info-icon{width:51px;height:51px;border-radius:50%;background:var(--green-dark);display:flex;align-items:center;justify-content:center}
.info-text{font-size:13.5px;line-height:18px;color:#333}
.info-text b{font-weight:600;display:block}

.footer{left:0;top:2523px;width:1200px;height:46px;background:var(--footer);color:#fff;font-size:13.5px}
.footer span{position:absolute;top:14px}
</style>
</head>
<body>

<header class="abs hero">
  <div class="hero-photo" role="img" aria-label="Foto einer jungen Frau am Steuer eines Autos, rechts eine leuchtend grüne Cannabispflanze, grün eingefärbt"></div>
  <svg class="hero-band" width="1200" height="537" aria-hidden="true"><polygon points="0,537 0,470 840,400 1200,440 1200,537" fill="#6a8f63" opacity=".9"/></svg>
  <div class="abs brand">RV-Vitalis</div>
  <h1 class="abs heading hero-title">Mach den<br>Selbsttest.</h1>
  <div class="abs hero-sub">Gefährde nicht deinen Führerschein!</div>
  <svg class="abs bubble" width="180" height="145" aria-hidden="true">
    <path d="M18,55 C5,110 70,150 140,135 C165,125 150,80 130,60 Z" fill="#6a8f63" opacity=".8"/>
    <path d="M30,20 C70,-10 170,0 176,45 C182,90 150,140 80,135 C20,130 -5,60 30,20 Z" fill="var(--cream)"/>
  </svg>
  <div class="abs heading bubble-text">Im Straßen&shy;verkehr liegt die Grenze bei 3,5ng/ml.</div>
</header>

<div class="abs partner" style="left:110px;width:125px"></div>
<div class="abs partner" style="left:330px;width:175px"></div>
<div class="abs partner" style="left:603px;width:145px"></div>
<div class="abs partner" style="left:842px;width:62px"></div>
<div class="abs partner" style="left:990px;width:118px"></div>

<section class="abs tile" style="left:88px;top:657px;width:509px;height:468px">
  <div class="tile-fill" role="img" aria-label="Gruppenfoto lachender junger Menschen, grün eingefärbt" style="background:linear-gradient(180deg,#3e7a35 0%,#2f6428 55%,#214a1c 100%)"></div>
  <h2 class="abs heading tile-title" style="left:36px;top:312px">Gemeinsam<br>für mehr Sicherheit.</h2>
  <div class="abs tile-sub" style="left:36px;top:400px">Für euch und eurer Zukunft.</div>
</section>

<section class="abs" style="left:645px;top:716px;width:475px">
  <h2 class="heading section-title">Wir sind für euch da.</h2>
  <div class="rule" style="margin:12px 0 32px"></div>
  <div class="copy">
    <p>Ihr benötigt qualitativ hochwertige Produkte? RV-Vitalis ist für Sie da. Wir bieten geprüfte Hilfsmittel für Heimanwender, Testzentren, Ärzte, Krankenhäuser und Gewerbetreibende, mit denen Sie sicher durch den Alltag kommen.</p>
    <p>Durch die Gesetzesänderung in Bezug auf Cannabis werden Drogenschnelltests in Zukunft in bestimmten Situationen unverzichtbar sein. Bestellen Sie bei uns hochwertige Schnelltests auf z.B. THC oder Amphetamine zu attraktiven Preisen.</p>
    <p>Unser Fachpersonal unterstützt Sie gerne bei Fragen zu unserem Sortiment. Mit 11 Jahren Erfahrung unterstützen wir Sie gerne bei der umfassenden Pandemie- und Gesundheitsvorsorge.</p>
    <p>Moderne Produkte und hohe Fertigungsstandards gepaart mit qualifiziertem Service.</p>
  </div>
</section>

<section class="abs" style="left:107px;top:1229px;width:470px">
  <h2 class="heading section-title">THC Drogenschnelltest 5ng (Cannabis, Marihuana, Haschisch), 5 ng/m</h2>
  <div class="rule" style="margin:14px 0 30px"></div>
  <div class="copy" style="font-size:13.4px;line-height:20px">
    <p>Ein THC-Urintest ist ein diagnostisches Verfahren, mit dem Tetrahydrocannabinol (THC), der psychoaktive Wirkstoff von Cannabis, im Urin nachgewiesen werden kann. Der Test beruht auf der Tatsache, dass THC und seine Metaboliten nach dem Konsum von Cannabis noch einige Zeit im Körper verbleiben und über den Urin ausgeschieden werden können.</p>
    <p>Der Test wird häufig eingesetzt, um den Konsum von Cannabis nachzuweisen, insbesondere bei Drogentests, am Arbeitsplatz oder in Gerichtsverfahren.</p>
    <p>Es ist wichtig zu beachten, dass ein positiver THC-Urintest nicht unbedingt bedeutet, dass die Person zum Zeitpunkt des Tests unter dem Einfluss von Cannabis steht, sondern lediglich, dass sie in der Vergangenheit Cannabis konsumiert hat.</p>
  </div>
</section>

<section class="abs tile" style="left:606px;top:1165px;width:509px;height:468px">
  <div class="tile-fill" role="img" aria-label="Foto einer Ärztin mit einem verpackten THC-Urintest im Vordergrund, grün eingefärbt" style="background:linear-gradient(135deg,#2f6428 0%,#3d7a36 45%,#8fb39a 75%,#2a5a24 100%)"></div>
  <h2 class="abs heading tile-title" style="left:37px;top:312px">Einfach und<br>unkompliziert</h2>
  <div class="abs tile-sub" style="left:37px;top:400px">Testergebnis nach 5 Minuten</div>
</section>

<a class="abs heading cta" href="https://www.rv-vitalis.de">Hier geht es zum Shop</a>

<h2 class="abs heading section-title" style="left:88px;top:1825px">Hast du Fragen?<br>Dann nimm doch Kontakt mit uns auf.</h2>
<div class="abs rule" style="left:88px;top:1898px"></div>

<div class="abs field" style="left:88px;top:1963px;width:288px;height:42px">Name</div>
<div class="abs field" style="left:388px;top:1963px;width:295px;height:42px">E-Mailadresse</div>
<div class="abs field" style="left:88px;top:2018px;width:595px;height:42px">Betreff</div>
<div class="abs field" style="left:88px;top:2073px;width:595px;height:230px">Ihre Nachricht</div>
<div class="abs check"></div>
<div class="abs consent">Ich akzeptiere die <a href="#">Datenschutzbestimmungen</a> und die Verarbeitung meiner Daten.</div>
<div class="abs heading send">Anfrage senden</div>

<div class="abs divider"></div>
<div class="abs brand contact-brand">RV-Vitalis</div>

<div class="abs info-icon" style="left:769px;top:2081px"><svg width="22" height="22" viewBox="0 0 24 24" fill="none" stroke="#fff" stroke-width="1.8"><path d="M12 22s7-7 7-12a7 7 0 0 0-14 0c0 5 7 12 7 12z"/><circle cx="12" cy="10" r="2.5"/></svg></div>
<div class="abs info-text" style="left:833px;top:2091px"><b>Adresse:</b>Lindenweg 12 , 18439 Musterstadt</div>

<div class="abs info-icon" style="left:769px;top:2157px"><svg width="22" height="22" viewBox="0 0 24 24" fill="none" stroke="#fff" stroke-width="1.8"><rect x="3" y="5" width="18" height="14" rx="2"/><path d="M3 7l9 6 9-6"/></svg></div>
<div class="abs info-text" style="left:833px;top:2167px"><b>E-Mail:</b>info[at]rvhandel.de</div>

<div class="abs info-icon" style="left:769px;top:2232px"><svg width="22" height="22" viewBox="0 0 24 24" fill="none" stroke="#fff" stroke-width="1.8"><path d="M5 3h4l2 5-2.5 1.5a11 11 0 0 0 6 6L16 13l5 2v4a2 2 0 0 1-2 2A17 17 0 0 1 3 5a2 2 0 0 1 2-2z"/></svg></div>
<div class="abs info-text" style="left:833px;top:2242px"><b>Telefon:</b>+49&nbsp; (0)800 55 21 480</div>

<div class="abs info-icon" style="left:769px;top:2300px"><svg width="22" height="22" viewBox="0 0 24 24" fill="none" stroke="#fff" stroke-width="1.8"><path d="M12 22s7-7 7-12a7 7 0 0 0-14 0c0 5 7 12 7 12z"/><circle cx="12" cy="10" r="2.5"/></svg></div>
<div class="abs info-text" style="left:833px;top:2310px"><b>Web:</b>www.rv-vitalis.de</div>

<footer class="abs footer">
  <span style="left:88px">© 2024 Medizin- und Praxisbedarf online kaufen - RV-Vitalis - Alle Rechte vorbehalten.</span>
  <span style="left:639px">Impressum</span>
  <span style="left:726px">Datenschutz</span>
  <span style="left:817px">Cookie-Richtlinie (EU)</span>
  <span style="left:1005px">Plauderbox</span>
  <span style="left:1078px">Zwitscherhaus</span>
</footer>

</body>
</html>
```